I need a logo, business card and letterhead designed. I've just started a Property Management business based in Sydney, Australia. My company name is KRV Management and I would love my name to be combined within the logo, not just two separate images. KRV stands for Kestrel Ridgeview Venture.The focus on my business is great service, although small right now, I believe it will definitely grow over time. I prefer simplicity and don't mind abstract designs, as long as they aren't too abstract. I would like it to convey a sense of professionalism yet a very 'down to earth company'
Updates

Target Market(s)

My service is to all clientele, generally the upper end of the market with investments in property. The age group would be around 35 years old and up. Also the Asian market as well, since I am bilingual in Chinese but the logo doesn't need to reflect that.

Industry/Entity Type

Business

Requirements
Must have
• The logo must still be able to look nice if printed in black and white/greyscale.
Nice to have
• I would love to see my company name combined in the logo. If there was any regency to Australian, I would love that. It could be the colour scheme representing the Australian beach or anything along those lines.
Should not have
• The design cannot be specific to one culture, for example, I don't like having chinese characters or cultural specific items in my logo, in that other people cannot understand it.

```html
<!DOCTYPE html>
<html lang="en">
<head>
<meta charset="utf-8">
<title>KRV Management – Stationery</title>
<link rel="stylesheet" href="https://fonts.googleapis.com/css2?family=Questrial&display=swap">
<style>
  :root{
    --bg:#e9ebed;
    --paper:#ffffff;
    --paper-shade:#f4f5f6;
    --brand-blue:#2a7ba6;
    --brand-grey:#6c6c6c;
    --text-grey:#8a8d90;
    --line-grey:#9c9fa2;
  }
  *{box-sizing:border-box;margin:0;padding:0}
  html,body{width:1200px;height:859px;overflow:hidden}
  body{background:var(--bg);font-family:"Questrial",Arial,sans-serif;position:relative}
  .sheet{position:absolute;background:var(--paper);box-shadow:0 2px 6px rgba(0,0,0,.12);overflow:hidden}

  .brand{display:flex;align-items:center;gap:8px;color:var(--brand-blue);white-space:nowrap}
  .brand-square{background:var(--brand-blue);flex:none}
  .brand-name{font-weight:400;letter-spacing:.02em}

  .strip{position:absolute;left:0;right:0;bottom:0;display:flex}
  .strip .grey{background:var(--brand-grey);flex:1}
  .strip .blue{background:var(--brand-blue)}

  .contact{color:var(--text-grey);font-size:7px;line-height:1.7}
  .contact li{list-style:none;display:flex;align-items:center;gap:4px}
  .dot{width:5px;height:5px;border-radius:50%;background:var(--brand-blue);flex:none}

  /* Letterhead */
  .letterhead{left:40px;top:40px;width:320px;height:452px}
  .letterhead .brand{position:absolute;left:30px;top:30px}
  .letterhead .brand-square{width:16px;height:16px}
  .letterhead .brand-name{font-size:17px}
  .letterhead .contact{position:absolute;left:30px;bottom:26px;display:flex;gap:22px}
  .letterhead .strip{height:8px}
  .letterhead .strip .blue{width:90px}

  /* Folder */
  .folder{left:400px;top:40px;width:340px;height:452px}
  .folder .brand{position:absolute;left:60px;top:70px}
  .folder .brand-square{width:24px;height:24px}
  .folder .brand-name{font-size:26px}
  .folder-band{position:absolute;left:0;right:0;top:150px;height:10px;display:flex}
  .folder-band .blue{background:var(--brand-blue);width:48%}
  .folder-band .grey{background:var(--brand-grey);flex:1}
  .folder-body{position:absolute;left:0;right:0;top:166px;bottom:0;background:var(--brand-grey)}

  /* Business cards */
  .card{width:300px;height:172px;left:820px}
  .card-a{top:40px}
  .card-b{top:250px}
  .card .brand{position:absolute;left:22px;top:22px}
  .card .brand-square{width:14px;height:14px}
  .card .brand-name{font-size:15px}
  .card .person{position:absolute;left:22px;top:58px}
  .card .person-name{color:var(--brand-blue);font-size:11px;letter-spacing:.06em;text-transform:uppercase}
  .card .person-role{color:var(--text-grey);font-size:8px;margin-top:2px}
  .card .contact{position:absolute;left:22px;top:94px}
  .card .strip{height:7px}
  .card .strip .blue{width:70px}

  /* Compliments slip */
  .slip{left:40px;top:540px;width:500px;height:250px}
  .slip .brand{position:absolute;left:40px;top:40px}
  .slip .brand-square{width:20px;height:20px}
  .slip .brand-name{font-size:22px}
  .slip .address{position:absolute;left:40px;bottom:34px;color:var(--text-grey);font-size:7px}
  .slip .strip{height:9px}
  .slip .strip .blue{width:110px}

  /* Envelope back */
  .envelope{left:600px;top:540px;width:520px;height:250px;background:var(--paper-shade)}
  .envelope-flap{position:absolute;left:0;right:0;top:0;height:110px;background:var(--brand-grey);display:flex;align-items:center;justify-content:center}
  .envelope-flap .mark{width:16px;height:16px;background:#d6d8da}
</style>
</head>
<body>

  <section class="sheet letterhead" aria-label="Letterhead">
    <div class="brand"><span class="brand-square"></span><span class="brand-name">KRV Management</span></div>
    <div class="contact">
      <ul><li><span class="dot"></span>+61 2 5550 1742</li><li><span class="dot"></span>+61 2 5550 1743</li></ul>
      <ul><li><span class="dot"></span>info@krvmanagement.com</li><li><span class="dot"></span>www.krvmanagement.com</li></ul>
      <ul><li>18 Harbourline Place, Level 4</li><li>Sydney NSW 2000</li></ul>
    </div>
    <div class="strip"><span class="grey"></span><span class="blue"></span></div>
  </section>

  <section class="sheet folder" aria-label="Presentation folder">
    <div class="brand"><span class="brand-square"></span><span class="brand-name">KRV Management</span></div>
    <div class="folder-band"><span class="blue"></span><span class="grey"></span></div>
    <div class="folder-body"></div>
  </section>

  <section class="sheet card card-a" aria-label="Business card">
    <div class="brand"><span class="brand-square"></span><span class="brand-name">KRV Management</span></div>
    <div class="person"><p class="person-name">Jonah Reyes</p><p class="person-role">Property Manager</p></div>
    <ul class="contact">
      <li><span class="dot"></span>+61 2 5550 1742</li>
      <li><span class="dot"></span>info@krvmanagement.com</li>
      <li><span class="dot"></span>18 Harbourline Place, Sydney NSW 2000</li>
    </ul>
    <div class="strip"><span class="grey"></span><span class="blue"></span></div>
  </section>

  <section class="sheet card card-b" aria-label="Business card">
    <div class="brand"><span class="brand-square"></span><span class="brand-name">KRV Management</span></div>
    <div class="person"><p class="person-name">Jonah Reyes</p><p class="person-role">Property Manager</p></div>
    <ul class="contact">
      <li><span class="dot"></span>+61 2 5550 1742</li>
      <li><span class="dot"></span>info@krvmanagement.com</li>
      <li><span class="dot"></span>18 Harbourline Place, Sydney NSW 2000</li>
    </ul>
    <div class="strip"><span class="grey"></span><span class="blue"></span></div>
  </section>

  <section class="sheet slip" aria-label="Compliments slip">
    <div class="brand"><span class="brand-square"></span><span class="brand-name">KRV Management</span></div>
    <p class="address">18 Harbourline Place, Level 4, Sydney NSW 2000</p>
    <div class="strip"><span class="grey"></span><span class="blue"></span></div>
  </section>

  <section class="sheet envelope" aria-label="Envelope back">
    <div class="envelope-flap"><span class="mark"></span></div>
  </section>

</body>
</html>
```